A website for a catering company called "Fenwick's Catering"

1. We need a website for a very well established, high-end outside catering company - Fenwick's Catering.
2. Fenwick's Catering has been trading for 30yrs+ and is based in the riverside town of Upton upon Severn in Worcestershire, UK. The founders of the business are Marnie and Jo Fenwick. Marnie and Jo are sisters.
They only use locally sourced and sustainable ingredients wherever possible and offer a bespoke catering service. All of their food is created at the company's dedicated kitchen premises. No food is "bought-in", it is all prepared by hand from the basic ingredients.
3. Typical functions catered for include weddings, anniversaries, special occasions such as parties, corporate events, funerals etc. All of Fenwick's Catering's clients are spoken to and then visited personally to discuss details of their bespoke event. The company does NOT provide low-end, pile it high, sell it cheap food!
4. Fenwick's Catering does not advertise in any way, except by word of mouth. It requires a website to provide a simple web presence to allow potential clients to contact the company via email in the modern digital age!
5. The site needs to work on PC, tablet and mobile devices.
6. The site needs to be of a modern yet contemporary and high-class design and also be very intuitive to navigate.
7. The site only needs 2 main pages - an elegant/contemporary landing page that contains a "contact us" button to link to a 2nd page requiring the reader to complete a contact form to automatically email the company. The contact form must be protected from spamming via some sort of captcha type function and it must contain a mandatory field for the enquirer's telephone number - all of the company's clients are spoken to and then visited personally to discuss details of events.
8. The website must not require any routine maintenance - the simpler the better!
9. We have already secured the URL: www.fenwickscatering.co.uk to host a website. However, this URL has not been hosted yet. The website contact form will need to auto email marnie@fenwickscatering.co.uk .
10. Below are a few websites which we like the look of, just to give you an idea of the kind of style we're after:
http://www.quarrymeadinn.co.uk/
http://thegreenoakbrampley.co.uk/
http://www.dunmorekitchen.com/
http://www.thelantry.co.uk/
http://www.thefiddlerinn.co.uk/
11. We've also attached some images of events catered at and some images that we've captured ourselves to give you other ideas of look and feel. We're not precious about these being used for the site, so that's up to you!

Target Market(s)

High class, bespoke outside catering service. Typically affluent persons requiring a turn-key catering solution for a special function or event.

Industry/Entity Type

Catering

Coding

Coded - Design and coding required

Number of Pages Required

2 page

Font styles to use
Sans Serif

Requirements
Must have
• 1. The site needs to work on PC, tablet and mobile devices.
• 2. The site needs to be of a modern yet contemporary and high-class design and also be very intuitive to navigate.
• 3. The site only needs 2 main pages - an elegant/contemporary landing page that contains a "contact us" button to link to a 2nd page requiring the reader to complete a contact form to automatically email the company.
• 4. The contact form must be protected from spamming via some sort of captcha type function and it must contain a mandatory field for the enquirer's telephone number - all of the company's clients are spoken to and then visited personally to discuss details of events.
• 5. The website must not require any routine maintenance - the simpler the better!
• 6. We have already secured the URL: www.fenwickscatering.co.uk to host a website. However, this URL has not been hosted yet. The website contact form will need to auto email marnie@fenwickscatering.co.uk .
Nice to have
• Must look upmarket, with a contemporary modern feel. Striking images and minmal text - a clean, modern look.
Should not have
• Look old fashioned or dull.

```html
<!DOCTYPE html>
<html lang="en">
<head>
<meta charset="utf-8">
<title>Contact Us – Fenwick's Catering</title>
<link rel="stylesheet" href="https://fonts.googleapis.com/css2?family=Roboto:wght@300;400;500&family=Raleway:wght@500&display=swap">
<style>
  :root {
    --lime: #b3d651;
    --peach: #fddb9a;
    --nav-dark: #16181b;
    --nav-line: #2e3136;
    --ink: #1d1d1d;
    --panel: rgba(238, 238, 238, 0.88);
    --form-bg: #f4f4f4;
    --field-border: #d6d6d6;
    --orange: #f7900f;
    --footer: #050505;
    --topbar: rgba(225, 225, 225, 0.9);
  }
  * { box-sizing: border-box; margin: 0; padding: 0; }
  html, body { width: 1200px; height: 794px; overflow: hidden; }
  body { position: relative; font-family: 'Roboto', Arial, sans-serif; color: var(--ink); background: #ddd; }

  .hero-photo {
    position: absolute; inset: 0 0 76px 0;
    background:
      radial-gradient(ellipse at 70% 20%, rgba(120,150,70,0.9), transparent 60%),
      linear-gradient(180deg, #4b5a32 0%, #5d6b3c 35%, #8a8a78 55%, #c9c6c8 70%, #dcd9dc 100%);
  }
  .top-bar {
    position: absolute; left: 0; top: 0; width: 1200px; height: 50px;
    background: var(--topbar); font-size: 13px;
  }
  .top-bar .bookings { position: absolute; left: 379px; top: 19px; }
  .top-bar .account { position: absolute; left: 988px; top: 18px; }

  .sidebar { position: absolute; left: 99px; top: 0; width: 259px; }
  .sidebar .accent { height: 50px; background: var(--lime); }
  .logo {
    height: 87px; background: var(--peach);
    display: flex; align-items: center; justify-content: center; gap: 10px;
    font-size: 24px; font-weight: 400; color: #222;
  }
  .logo .dot { width: 14px; height: 14px; border-radius: 50%; background: var(--lime); }
  .main-nav { background: linear-gradient(180deg, #22262a, #050505); }
  .main-nav a {
    display: block; height: 50px; line-height: 50px; text-align: center;
    color: #fff; text-decoration: none; font-size: 15px;
    border-bottom: 1px solid var(--nav-line);
  }
  .main-nav a:last-child { border-bottom: 0; height: 56px; line-height: 52px; }
  .main-nav a.current { color: var(--lime); }

  .promo { position: absolute; left: 99px; top: 454px; width: 259px; }
  .promo-photo {
    height: 208px;
    background: linear-gradient(160deg, #e9e4da 0%, #c8a77c 45%, #8c8a55 75%, #d9c6a8 100%);
  }
  .promo-bar {
    height: 45px; background: var(--peach); display: flex; align-items: center;
    justify-content: space-between; padding: 0 9px 0 24px; font-size: 15px;
  }

  .address-card {
    position: absolute; left: 380px; top: 248px; width: 450px; height: 367px;
    background: var(--panel); border-radius: 8px; padding: 24px 0 0 41px;
  }
  .address-card h2 { font-size: 19px; font-weight: 400; margin-bottom: 14px; }
  .address-card .lines { font-size: 18px; font-weight: 300; line-height: 27px; color: #333; }
  .address-card .contacts { font-size: 18px; font-weight: 300; line-height: 35px; margin-top: 6px; color: #333; }
  .address-card .blurb { font-size: 13px; line-height: 22px; width: 390px; margin-top: 18px; color: #333; }

  .contact-form {
    position: absolute; left: 822px; top: 188px; width: 266px; height: 427px;
    background: var(--form-bg); border-radius: 10px;
  }
  .form-title {
    position: absolute; left: -12px; top: 19px; width: 290px; height: 43px;
    background: repeating-linear-gradient(135deg, #2a2a2a 0 2px, #333 2px 4px);
    color: #fff; font-family: 'Raleway', Arial, sans-serif; font-weight: 500;
    font-size: 19px; padding: 9px 0 0 32px;
  }
  .fields { position: absolute; left: 20px; top: 69px; width: 232px; }
  .fields label { display: block; font-size: 12px; margin-bottom: 2px; }
  .fields .input {
    height: 28px; background: #fff; border: 1px solid var(--field-border); margin-bottom: 8px;
  }
  .fields .textarea { height: 67px; }
  .captcha {
    width: 168px; height: 66px; margin-top: 7px; background: #9b1b1b;
    border-radius: 3px; padding: 3px; position: relative;
  }
  .captcha .challenge { height: 32px; background: linear-gradient(90deg, #fff, #e8e8e8); }
  .captcha .answer {
    position: absolute; left: 4px; top: 38px; width: 93px; height: 24px;
    background: #f6d27a; font-size: 6px; padding: 2px 4px;
  }
  .captcha .answer span { display: block; margin-top: 2px; height: 8px; width: 80px; background: #fff; border: 1px solid #888; }
  .captcha .badge { position: absolute; right: 6px; top: 41px; width: 44px; height: 18px; background: #b54040; }
  .submit {
    margin-top: 12px; width: 92px; height: 25px; background: var(--orange);
    color: #fff; font-size: 12px; text-align: center; line-height: 25px;
  }

  .site-footer {
    position: absolute; left: 0; bottom: 0; width: 1200px; height: 76px;
    background: var(--footer); color: #fff;
  }
  .social { position: absolute; left: 104px; top: 29px; display: flex; gap: 7px; }
  .social span {
    width: 31px; height: 31px; border-radius: 50%; background: #fff;
    border: 2px dashed #000; outline: 1px solid #fff;
  }
  .copyright { position: absolute; left: 933px; top: 38px; font-size: 13px; }
</style>
</head>
<body>
  <div class="hero-photo" role="img" aria-label="Garden party table with cakes and scones beneath a blossoming tree"></div>

  <header class="top-bar">
    <span class="bookings">Bookings and reservations: 01684 592710</span>
    <span class="account">Log in &nbsp;|&nbsp; Register</span>
  </header>

  <aside class="sidebar">
    <div class="accent"></div>
    <div class="logo"><span class="dot"></span>Fenwick's Catering</div>
    <nav class="main-nav">
      <a href="#">HOME</a>
      <a href="#">ABOUT US</a>
      <a href="#">PRODUCTS</a>
      <a href="#">ORDER</a>
      <a href="#">NEWS</a>
      <a href="#" class="current">CONTACT US</a>
    </nav>
  </aside>

  <section class="promo">
    <div class="promo-photo" role="img" aria-label="Wedding marquee with long tables, wooden chairs and wildflower posies"></div>
    <div class="promo-bar">
      <span>WEDDINGS SPECIAL</span>
      <svg width="30" height="30" viewBox="0 0 30 30" aria-hidden="true">
        <circle cx="15" cy="15" r="13" fill="none" stroke="#000" stroke-width="2.5"/>
        <path d="M12.5 9.5 L18 15 L12.5 20.5" fill="none" stroke="#000" stroke-width="2.5"/>
      </svg>
    </div>
  </section>

  <section class="address-card">
    <h2>ADDRESS</h2>
    <div class="lines">Fenwick's Catering<br>8 Riverside Walk,Upton upon Severn<br>&nbsp;WR8 0HG</div>
    <div class="contacts">
      Telephone : 01684 592 700<br>
      Fax : 01684 592 701<br>
      Email : info@fenwickscatering.co.uk
    </div>
    <p class="blurb">&nbsp;Lorem Ipsum has been the industry's standard dummy text ever since the 1500s, when an unknown printer took a galley of type and scrambled it to make a type specimen book.</p>
  </section>

  <section class="contact-form">
    <div class="form-title">Contact form</div>
    <div class="fields">
      <label>Your Name</label><div class="input"></div>
      <label>Your Email ID</label><div class="input"></div>
      <label>Contact No.</label><div class="input"></div>
      <label>Message</label><div class="input textarea"></div>
      <div class="captcha">
        <div class="challenge" role="img" aria-label="Distorted verification words"></div>
        <div class="answer">Type the two words:<span></span></div>
        <div class="badge"></div>
      </div>
      <div class="submit">SUBMIT</div>
    </div>
  </section>

  <footer class="site-footer">
    <div class="social"><span></span><span></span><span></span></div>
    <div class="copyright">Copyright © 2015 All Rights</div>
  </footer>
</body>
</html>
```